Xtreme Web Design

We require a web designer to create a new website design template for our business. A mixture of stock images, our images and graphic will be used. We would like a 'home' page that will stand out and a common base page design for all other pages in our site. We need to keep our current logo and will be looking for designs that stand out and relate directly to our industry (xtreme fast indoor go kart racing). We have also attached our current font that is used in our brochures and may or may not be used in your design.
We are currently opening another new facility and will be able to provide a lot of good quality racing, facility related and go kart images soon, but until then please obtain general images or images from our current site (www.bramblequayleisure.com.au) as required.
The design we need to be unique and sharp with options/ideas of various jquery plugins that we will utilize.
Reason: Being close to the busy xmas period, we have not been able to give fair feedback to some designs and would like to extend the deadline to allow for this. I thank you for your understanding.

```html
<!DOCTYPE html>
<html lang="en">
<head>
<meta charset="utf-8">
<title>Special Offers – Bramble Quay Karting</title>
<link rel="stylesheet" href="https://fonts.googleapis.com/css2?family=Righteous&family=Lato:wght@300;400&display=swap">
<style>
:root{
  --sky:#00a0e4;
  --navy:#15158a;
  --royal:#1d4fe0;
  --black:#111111;
  --white:#ffffff;
  --text:#333333;
  --brand:#1e8fe6;
}
*{box-sizing:border-box;margin:0;padding:0}
html,body{width:1200px;height:996px;overflow:hidden;background:var(--white)}
body{position:relative;font-family:"Lato",sans-serif;font-weight:300;color:var(--text)}
.display{font-family:"Righteous",sans-serif;font-weight:400}

.topbar{position:absolute;left:66px;top:0;width:1065px;height:42px;background:var(--sky)}
.social{position:absolute;left:14px;top:9px;display:flex;gap:6px}
.social span{width:24px;height:24px;background:var(--black);display:block}
.search{position:absolute;left:794px;top:9px;width:223px;height:25px;background:var(--white)}
.search-icon{position:absolute;left:1026px;top:9px}

.navbar{position:absolute;left:66px;top:42px;width:1065px;height:92px;background:var(--black)}
.logo{position:absolute;left:16px;top:30px;font-size:30px;color:var(--brand);letter-spacing:.5px}
.nav{position:absolute;left:380px;top:0;display:flex;height:92px;list-style:none}
.nav li{height:92px;display:flex;align-items:center;padding:0 21px;color:var(--white);font-size:18px;letter-spacing:.3px}
.nav li.active{background:var(--sky);margin-right:2px}

.hero{position:absolute;left:66px;top:134px;width:1065px;height:150px;background:linear-gradient(90deg,#8a8a8a,#5a5a5a 45%,#2a2a2a 55%,#9a9a9a 80%,#6c6c6c)}
.hero-title{position:absolute;left:66px;top:192px;height:50px}
.hero-title h1{position:absolute;left:32px;top:4px;font-size:40px;color:var(--white);white-space:nowrap;letter-spacing:.5px;font-weight:400}

.offers{position:absolute;left:68px;top:334px;width:420px}
.offer h2{font-size:23px;color:var(--navy);letter-spacing:.8px;margin-bottom:6px;font-weight:400}
.offer p{font-size:15px;line-height:19px}
.offer .cond{color:var(--navy);font-weight:400;margin-top:18px}
.offer ul{list-style:none;font-size:15px;line-height:19px}
.offer ul li::before{content:"\2022 "}
.offer + .offer{margin-top:38px}

.gallery{position:absolute;left:520px;top:327px;width:610px;height:468px;background:linear-gradient(180deg,#e9edf0 0%,#cfd5da 40%,#8f8a86 75%,#b9b6b2 100%)}
.arrow{position:absolute;top:522px;width:41px;height:52px;background:var(--royal);color:var(--white);font-size:17px;display:flex;align-items:center;justify-content:center}
.arrow.prev{left:514px}
.arrow.next{left:1094px}

.footer{position:absolute;left:0;top:823px;width:1200px;height:173px;background:var(--black);color:var(--white)}
.footer .logo{left:86px;top:50px;font-size:32px}
.address{position:absolute;right:87px;top:30px;text-align:right;font-size:16px;line-height:19px;letter-spacing:1px}
.copyright{position:absolute;left:68px;top:124px;font-size:14px;font-weight:400}
.legal{position:absolute;right:82px;top:124px;font-size:14px;font-weight:400}
</style>
</head>
<body>
<header>
  <div class="topbar">
    <div class="social"><span></span><span></span></div>
    <div class="search"></div>
    <svg class="search-icon" width="26" height="26" viewBox="0 0 26 26"><circle cx="15" cy="10" r="7" fill="none" stroke="#fff" stroke-width="2.5"/><line x1="10" y1="15" x2="3" y2="22" stroke="#fff" stroke-width="3.5" stroke-linecap="round"/></svg>
  </div>
  <div class="navbar">
    <div class="logo display">Bramble Quay Karting</div>
    <ul class="nav display">
      <li>PRICING</li>
      <li class="active">SPECIALS</li>
      <li>GROUP EVENTS</li>
      <li>LOCATIONS</li>
      <li>ABOUT US</li>
    </ul>
  </div>
</header>

<section>
  <div class="hero" role="img" aria-label="Black and white photo of karts racing on an indoor track"></div>
  <div class="hero-title">
    <svg width="406" height="50" viewBox="0 0 406 50"><polygon points="0,0 356,0 336,50 0,50" fill="#15158a"/><polygon points="364,0 376,0 356,50 344,50" fill="#15158a"/><polygon points="384,0 396,0 376,50 364,50" fill="#15158a"/></svg>
    <h1 class="display">SPECIAL OFFERS</h1>
  </div>
</section>

<main>
  <div class="offers">
    <article class="offer">
      <h2 class="display">$5 OFF WEEKDAY GRID PRIX</h2>
      <p>Book a weekday Grand Prix and receive $5 off each driver.</p>
      <p class="cond">Conditions:</p>
      <ul>
        <li>Must mention offer when booking</li>
        <li>Not available weekends or public holidays</li>
        <li>Min 6 drivers must race</li>
        <li>$10 deposit required for each driver when making booking</li>
        <li>Not valid through Dec/Jan</li>
      </ul>
    </article>
    <article class="offer">
      <h2 class="display">FREE FUNCTION ROOM</h2>
      <p>Book a weekday Grand Prix and receive free access to the function room overlooking the track.</p>
      <p class="cond">Conditions:</p>
      <ul>
        <li>Must mention offer when booking</li>
        <li>Not available weekends or public holidays</li>
        <li>Min 12 drivers must race</li>
        <li>$10 deposit required for each driver when making booking</li>
        <li>No BYO food allowed in function room</li>
        <li>Not valid through Dec/Jan</li>
      </ul>
    </article>
  </div>
  <div class="gallery" role="img" aria-label="Photo of a group of guests posing together in the venue lobby"></div>
  <div class="arrow prev">&lt;</div>
  <div class="arrow next">&gt;</div>
</main>

<footer class="footer">
  <div class="logo display">Bramble Quay Karting</div>
  <div class="address display">24 FENWICK<br>LANE ASHCOMBE<br>417 LINDEN<br>RD CORROW POINT</div>
  <div class="copyright">Copyright (C) 2013 bramblequay.com</div>
  <div class="legal">Privacy | Terms and Conditions | Disclaimer | Copyright Notice | Cookies Policy | Linking Policy</div>
</footer>
</body>
</html>
```